Business card design for web travel company

Hi
we'd like to receive some proposal for a business card design.
Stayvano is a private travel club, dedicated to all travel lovers, with unique offers for exclusive destinations all around the world. At Stayvano you can find a wide range of offers for resorts, boutique hotels and travel packages at the best guaranteed price available on the market. The convenience of the offer is guaranteed by a private sales model: offers are available for a limited time only and they are personally chosen by Stayvano's qualified team of travel experts.
We offer only exclusive hotels with discounted prices but we are not an outlet or a discount supermarket: the design should reflect our connection with luxury, exclusivity using the same style of our website www.stayvano-example.com.
We want to make sure that when we'll present ourself to our business partner they will feel immediately which is our brand positioning giving them also a sense of an affordable and reliable partner.
In attachment you can also find our brand guidelines (please note that we are NOT USING ANY MORE THE TAG LINE "Five star outlet" mentioned in it).
The info to be inserted are:
Name Surname
Job Title
Tel
Mobile (when needed)
Email
Stayvano S.r.l.
Via Bruno Lesta 27
20131 Milano

```html
<!DOCTYPE html>
<html lang="en">
<head>
<meta charset="utf-8">
<title>Stayvano – Business Card</title>
<link rel="stylesheet" href="https://fonts.googleapis.com/css2?family=Arimo:wght@400&display=swap">
<style>
  :root {
    --page: #ffffff;
    --card-light: #5b5b5b;
    --card-mid: #3f3f3f;
    --card-dark: #2b2b2b;
    --gold: #b9a66f;
    --gold-soft: #a8965f;
    --ink-light: #ffffff;
    --ink-dark: #333333;
    --rule: #9a9a9a;
  }
  * { margin: 0; padding: 0; box-sizing: border-box; }
  html, body {
    width: 1200px;
    height: 900px;
    overflow: hidden;
    background: var(--page);
    font-family: "Arimo", Arial, sans-serif;
  }
  .card {
    position: absolute;
    left: 30px;
    top: 84px;
    width: 1134px;
    height: 732px;
    overflow: hidden;
    background: radial-gradient(circle at 22% 40%, var(--card-light) 0%, var(--card-mid) 45%, var(--card-dark) 100%);
  }
  .brand {
    position: absolute;
    left: 60px;
    top: 70px;
    font-size: 80px;
    font-weight: 400;
    color: var(--ink-light);
    letter-spacing: 1px;
    line-height: 1;
  }
  .divider {
    position: absolute;
    left: 618px;
    top: 226px;
    width: 2px;
    height: 274px;
    background: var(--rule);
  }
  .contact {
    position: absolute;
    left: 640px;
    width: 460px;
    top: 232px;
    text-align: center;
    color: var(--ink-light);
  }
  .contact__name { font-size: 50px; line-height: 1.1; }
  .contact__role { font-size: 28px; margin-top: 6px; }
  .contact__lines { list-style: none; margin-top: 54px; font-size: 28px; line-height: 39px; }
  .ornament {
    position: absolute;
    left: 0;
    bottom: 0;
    width: 1134px;
    height: 310px;
  }
  .footer-address {
    position: absolute;
    left: 0;
    right: 0;
    bottom: 18px;
    text-align: center;
    padding-right: 150px;
    font-size: 28px;
    color: var(--ink-dark);
  }
</style>
</head>
<body>
  <section class="card">
    <div class="brand">Stayvano</div>

    <div class="divider"></div>

    <div class="contact">
      <h1 class="contact__name" style="font-weight:400">Luca Moretti</h1>
      <p class="contact__role">Manager</p>
      <ul class="contact__lines">
        <li>Tel: 02 - 555 - 0147</li>
        <li>Mobile: 333 - 555 - 0182</li>
        <li>Email: info@stayvano-example.com</li>
      </ul>
    </div>

    <svg class="ornament" viewBox="0 0 1134 310" role="img" aria-label="Gold flourish ornament with swirls, dots and leaves rising from a wave along the bottom edge">
      <defs>
        <linearGradient id="ornament-fade" x1="0" y1="0" x2="0" y2="1">
          <stop offset="0" stop-color="#b9a66f" stop-opacity="0"/>
          <stop offset="0.55" stop-color="#b9a66f" stop-opacity="0.35"/>
          <stop offset="1" stop-color="#b9a66f" stop-opacity="0.9"/>
        </linearGradient>
      </defs>
      <rect x="0" y="0" width="1134" height="310" fill="url(#ornament-fade)"/>
      <rect x="0" y="250" width="1134" height="60" fill="#b9a66f"/>
    </svg>

    <p class="footer-address">Stayvano S.r.l. Via Bruno Lesta 27, 20131 Milano</p>
  </section>
</body>
</html>
```